QRN Law Letterhead

Want law firm letterhead - both in terms of a pdf file that I can use electronically as letterhead by adding it as a background - and in terms of a file that I can send to a company to create actual letterhead.
Industry/Entity Type
Law Firm
Font styles to use
Sans Serif
Requirements
Must have
- Should have the following information (you can decide where to place):
- My name - Emil Vostrakian
- My email - emil@qrnlegalgroup.example
- My address - 2861 Corvella Parkway 318-742
- San Jose, California 95342
- Website - www.qrnlegalgroup.example
- Phone - 408-297-1586
- Fax - 408-853-2941
- The logo I attached
Nice to have
- I think I would prefer to have a black and white color scheme.
- I don't necessarily need a title after my name, but I have seen a few design submissions that include a generic title. The title I would use is "IP Litigator & Trademark Attorney"

```html
<!DOCTYPE html>
<html lang="en">
<head>
<meta charset="utf-8">
<title>QRN Law Letterhead</title>
<link rel="stylesheet" href="https://fonts.googleapis.com/css2?family=Bitter:wght@400;500&family=Montserrat:wght@500&display=swap">
<style>
  :root {
    --brand: #5b7b8f;
    --brand-dark: #4f6f83;
    --text: #4d6577;
    --paper: #ffffff;
    --on-brand: #ffffff;
  }
  html, body {
    margin: 0;
    padding: 0;
    overflow: hidden;
    background: var(--paper);
  }
  .letterhead {
    position: relative;
    width: 853px;
    height: 1200px;
    background: var(--paper);
    overflow: hidden;
    font-family: "Bitter", Georgia, serif;
    color: var(--text);
  }
  .brand {
    position: absolute;
    left: 40px;
    top: 50px;
    height: 84px;
    display: flex;
    align-items: center;
    gap: 12px;
  }
  .brand-mark {
    width: 84px;
    height: 84px;
    border-radius: 50%;
    background: var(--brand);
  }
  .brand-name {
    font-family: "Montserrat", Arial, sans-serif;
    font-size: 48px;
    font-weight: 500;
    color: var(--brand);
    line-height: 1;
    white-space: nowrap;
  }
  .contact {
    position: absolute;
    left: 574px;
    top: 64px;
    margin: 0;
    padding: 0;
    list-style: none;
  }
  .contact li {
    display: flex;
    align-items: center;
    height: 26px;
    font-size: 17px;
    white-space: nowrap;
  }
  .contact li.contact-small { font-size: 15px; }
  .contact svg {
    width: 18px;
    height: 18px;
    margin-right: 11px;
    flex: none;
    fill: none;
    stroke: var(--brand);
    stroke-width: 1.6;
  }
  .contact svg .solid { fill: var(--brand-dark); stroke: none; }
  .footer-band {
    position: absolute;
    left: 136px;
    top: 1108px;
    width: 690px;
    height: 76px;
    background: var(--brand);
  }
  .footer-mark {
    position: absolute;
    left: 38px;
    top: 1100px;
    width: 92px;
    height: 92px;
    border-radius: 50%;
    background: var(--brand);
  }
  .address {
    position: absolute;
    left: 235px;
    top: 1120px;
    width: 400px;
    text-align center;
    text-align: center;
    color: var(--on-brand);
    font-size: 17px;
    line-height: 27px;
    font-style: normal;
    white-space: nowrap;
  }
</style>
</head>
<body>
<main class="letterhead">
  <header class="brand">
    <div class="brand-mark"></div>
    <div class="brand-name">QRN Law</div>
  </header>

  <ul class="contact">
    <li>
      <svg viewBox="0 0 18 18"><circle class="solid" cx="9" cy="5" r="3.6"/><path class="solid" d="M3 17c0-4 2.7-7 6-7s6 3 6 7z"/></svg>
      Emil Vostrakian
    </li>
    <li>
      <svg viewBox="0 0 18 18"><rect x="1.5" y="3.5" width="15" height="11" rx="1"/><path d="M1.5 4l7.5 6 7.5-6"/></svg>
      emil@qrnlegalgroup.example
    </li>
    <li class="contact-small">
      <svg viewBox="0 0 18 18"><path d="M4 2l3 3-2 2c1 2.5 3.5 5 6 6l2-2 3 3-2 2.5C8 16 2 10 1.5 4z"/></svg>
      408-297-1586
    </li>
    <li class="contact-small">
      <svg viewBox="0 0 18 18"><rect x="2" y="6" width="14" height="9" rx="1"/><rect x="5" y="2" width="8" height="4"/><path d="M5 9h8M5 12h5"/></svg>
      408-853-2941
    </li>
    <li class="contact-small">
      <svg viewBox="0 0 18 18"><circle cx="9" cy="9" r="7.2"/><path d="M1.8 9h14.4M9 1.8c-3 3.5-3 10.9 0 14.4M9 1.8c3 3.5 3 10.9 0 14.4"/></svg>
      www.qrnlegalgroup.example
    </li>
  </ul>

  <div class="footer-band"></div>
  <div class="footer-mark"></div>
  <address class="address">
    2861 Corvella Parkway 318-742<br>
    San Jose, California 95342
  </address>
</main>
</body>
</html>
```